" Visitamos clientes importadores e vendemos nossos servicos. Eles nos fornecem a factura a qual desejam importar e nos tratamos de todo o processo de desalfandegamento da mercadoria ate o transporte e entrega no armazem dos nossos clientes. "

```html
<!DOCTYPE html>
<html lang="pt">
<head>
<meta charset="utf-8">
<title>Zefora Trading – Autocolantes</title>
<link href="https://fonts.googleapis.com/css2?family=Montserrat:wght@400;700&display=swap" rel="stylesheet">
<style>
  :root {
    --navy: #1f2f8f;
    --white: #ffffff;
    --grey-mark: #8a8d94;
    --ring-soft: #b8bfe6;
    --backdrop: #e6e6e6;
  }
  * { box-sizing: border-box; margin: 0; padding: 0; }
  html, body {
    width: 1200px; height: 1200px; overflow: hidden;
    background: var(--backdrop);
    font-family: "Montserrat", Arial, sans-serif;
  }
  .sheet {
    width: 1200px; height: 1200px;
    display: flex; align-items: center; justify-content: center; gap: 60px;
  }
  .sticker {
    position: relative;
    width: 520px; height: 520px; border-radius: 50%;
    overflow: hidden;
  }
  .sticker::before {
    content: ""; position: absolute; inset: 22px; border-radius: 50%;
    border: 4px solid var(--ring);
  }
  .sticker--light { background: var(--white); --ring: var(--navy); --text: var(--navy); --faint: rgba(31,47,143,0.05); }
  .sticker--dark  { background: var(--navy); --ring: var(--ring-soft); --text: var(--white); --faint: rgba(255,255,255,0.07); }

  .sticker__backdrop-mark {
    position: absolute; width: 340px; height: 340px; border-radius: 50%;
    background: var(--faint); top: 60px; left: 90px;
  }
  .brand {
    position: absolute; left: 70px; top: 205px;
    display: flex; align-items: center; gap: 14px;
  }
  .brand__dot { width: 66px; height: 66px; border-radius: 50%; background: var(--grey-mark); flex: none; }
  .brand__lockup { display: flex; flex-direction: column; }
  .brand__name {
    color: var(--text); font-weight: 700; font-size: 42px; line-height: 1;
    letter-spacing: 2px;
  }
  .brand__name-sub {
    color: var(--text); font-weight: 700; font-size: 18px; line-height: 1;
    letter-spacing: 10px; margin-top: 6px;
  }
  .brand__tagline {
    color: var(--text); font-size: 8px; font-weight: 400; letter-spacing: 0.4px;
    margin-top: 6px; text-transform: uppercase; white-space: nowrap;
  }
  .contact {
    position: absolute; left: 150px; top: 300px;
    color: var(--text); font-size: 24px; font-weight: 400; letter-spacing: 1px;
    white-space: nowrap;
  }
  .contact__icon {
    position: absolute; left: 140px; top: 340px;
    width: 20px; height: 20px; fill: var(--text);
  }
</style>
</head>
<body>
<main class="sheet">
  <section class="sticker sticker--light">
    <div class="sticker__backdrop-mark" role="img" aria-label="Faint brand symbol decoration"></div>
    <div class="brand">
      <span class="brand__dot"></span>
      <div class="brand__lockup">
        <span class="brand__name">ZEFORA</span>
        <span class="brand__name-sub">TRADING</span>
        <span class="brand__tagline">Despachos aduaneiros &amp; transportes</span>
      </div>
    </div>
    <span class="contact">(00) 0000-0000</span>
    <svg class="contact__icon" viewBox="0 0 24 24" aria-hidden="true"><path d="M6.6 10.8a15.1 15.1 0 0 0 6.6 6.6l2.2-2.2a1 1 0 0 1 1-.25 11.4 11.4 0 0 0 3.6.57 1 1 0 0 1 1 1V20a1 1 0 0 1-1 1A17 17 0 0 1 3 4a1 1 0 0 1 1-1h3.5a1 1 0 0 1 1 1c0 1.25.2 2.45.57 3.6a1 1 0 0 1-.25 1z"/></svg>
  </section>

  <section class="sticker sticker--dark">
    <div class="sticker__backdrop-mark" role="img" aria-label="Faint brand symbol decoration"></div>
    <div class="brand">
      <span class="brand__dot"></span>
      <div class="brand__lockup">
        <span class="brand__name">ZEFORA</span>
        <span class="brand__name-sub">TRADING</span>
        <span class="brand__tagline">Despachos aduaneiros &amp; transportes</span>
      </div>
    </div>
    <span class="contact">(00) 0000-0000</span>
    <svg class="contact__icon" viewBox="0 0 24 24" aria-hidden="true"><path d="M6.6 10.8a15.1 15.1 0 0 0 6.6 6.6l2.2-2.2a1 1 0 0 1 1-.25 11.4 11.4 0 0 0 3.6.57 1 1 0 0 1 1 1V20a1 1 0 0 1-1 1A17 17 0 0 1 3 4a1 1 0 0 1 1-1h3.5a1 1 0 0 1 1 1c0 1.25.2 2.45.57 3.6a1 1 0 0 1-.25 1z"/></svg>
  </section>
</main>
</body>
</html>
```